IT services company requires Letterhead design

We need a professional letterhead designed to be used for general correspondence with customers, quotes, invoices etc. We are a new IT services company specialising in computer servicing and repairs and mobile and tablet repairs. Attached are templates that my printing company have supplied, my logos, an interpretation of our website for you to get a feel of the company. Details to be included on the letterhead are

Company Number – 4738261
VAT Number - 518337942
Registered Address – 14-16 Brambly Lane, London, E4 9QT

Phone – 01632 487215
Email – sales@quorvent.com
Web – www.quorvent.com

I would prefer for the top of the letterhead to just have the company logo on a white background and the rest of the details on the bottom of the letterhead but I am open to design ideas.

Thanks

```html
<!DOCTYPE html>
<html lang="en">
<head>
<meta charset="utf-8">
<title>Quorvent Letterhead</title>
<link rel="stylesheet" href="https://fonts.googleapis.com/css2?family=Open+Sans:ital,wght@0,700;1,700&display=swap">
<style>
  :root {
    --paper: #ffffff;
    --page-edge: #9a9a9a;
    --rule: #7a7a7a;
    --brand-blue: #29abe2;
    --ink-dark: #3b3b3d;
    --footer-text: #ffffff;
    --watermark: #ececec;
  }
  * { margin: 0; padding: 0; box-sizing: border-box; }
  html, body {
    width: 1200px;
    height: 1101px;
    overflow: hidden;
    background: var(--paper);
    font-family: "Open Sans", Arial, sans-serif;
  }
  .letterhead {
    position: absolute;
    left: 231px;
    top: 18px;
    width: 819px;
    height: 1062px;
    background: var(--paper);
    border: 1px solid var(--page-edge);
    overflow: hidden;
  }
  .header-rule {
    position: absolute;
    left: 0;
    right: 0;
    top: 74px;
    border-top: 1px solid var(--rule);
  }
  .brand {
    position: absolute;
    right: 18px;
    top: 20px;
    display: flex;
    align-items: center;
    gap: 6px;
    color: var(--brand-blue);
    font-weight: 700;
    font-size: 17px;
  }
  .brand-square {
    width: 12px;
    height: 12px;
    background: var(--ink-dark);
  }
  .watermark {
    position: absolute;
    left: 0;
    right: 0;
    top: 400px;
    display: flex;
    align-items: center;
    justify-content: center;
    gap: 22px;
    color: var(--watermark);
    font-weight: 700;
    font-size: 96px;
  }
  .watermark-square {
    width: 60px;
    height: 60px;
    background: var(--watermark);
  }
  .footer {
    position: absolute;
    left: 0;
    bottom: 0;
    width: 819px;
    height: 164px;
  }
  .footer svg { position: absolute; inset: 0; width: 100%; height: 100%; }
  .registration {
    position: absolute;
    right: 22px;
    top: 68px;
    color: var(--footer-text);
    font-style: italic;
    font-weight: 700;
    font-size: 14px;
    line-height: 20px;
    text-align: right;
  }
  .contact-line {
    position: absolute;
    left: 14px;
    right: 14px;
    top: 118px;
    color: var(--brand-blue);
    font-weight: 700;
    font-size: 12.5px;
    white-space: nowrap;
    letter-spacing: -0.1px;
  }
</style>
</head>
<body>
  <main class="letterhead">
    <div class="brand"><span class="brand-square"></span>Quorvent</div>
    <div class="header-rule"></div>

    <div class="watermark" aria-hidden="true"><span class="watermark-square"></span>Quorvent</div>

    <footer class="footer">
      <svg viewBox="0 0 450 90" preserveAspectRatio="none" aria-hidden="true">
        <path d="M0,48 C120,40 210,18 310,18 C380,18 425,26 450,34 L450,90 L0,90 Z" fill="var(--ink-dark)"/>
        <path d="M235,26 C320,2 405,2 450,22 L450,30 C405,12 320,10 235,26 Z" fill="var(--brand-blue)"/>
      </svg>
      <div class="registration">
        CN : 4738261<br>
        VN :518337942
      </div>
      <p class="contact-line">RA : 14-16 Brambly Lane, London, E4 9QT,&nbsp; Phone : 01632 487215 &nbsp;&nbsp; E-mail : sales@quorvent.com, Web : www.quorvent.com</p>
    </footer>
  </main>
</body>
</html>
```